Vorquel 820 practise with the goal to have business and people Lifted past the horizon

We need a logo design for business cards for a company based in Australia Called TALBrookWare. We specialise in cloud tech from th full Quenfield stack. i would like it to be close to quenfield colours and we specilise in Quenfield Vorquel 820 Client Outreach. the design should display the confidence an security of a cloud based company. the tag line of Lifted past the horizon in the company motto.

Target Market(s)

I am targeting small to medium business up to 250 staff. i do work for not for profit and standard business.

Industry/Entity Type

Professional Service

Contact Information for Business Card

TALBrookWare Pty Ltd
A.C.N. 47 218 390 516
PO Box 827
Harlowe Point 4291
Mobile: 0400382957
Email: Dermot@Talbrookware.example.com.au

Font styles to use
Sans Serif

Colors

Designer to choose colors to be used in the design.

Requirements
Must have
• as a cloud based business it needs to have the this as the main theme. the tag line of Liftedpast the horizon should show we look at empowering business to get the most out of the cloud to minimise the spend they have as the target for the business is business and not for profits who need the make the most of their spend.
• the attached pictures are to be a source of insperation and key areas
Nice to have
• Quenfield Vorquel 820 is the core product that we sell and implentent for our clients so the theme should complement the Quenfield Vorquel theme

```html
<!DOCTYPE html>
<html lang="en">
<head>
<meta charset="UTF-8">
<title>TALBrookWare Business Card</title>
<link href="https://fonts.googleapis.com/css2?family=Raleway:wght@700&family=Lato:wght@400;700&display=swap" rel="stylesheet">
<style>
  :root {
    --stage: #2b2b2b;
    --card: #ffffff;
    --sky: #00aeef;
    --brand-blue: #2f6fb8;
    --brand-green: #6cbd3f;
    --text-grey: #555555;
    --rule-grey: #777777;
    --icon-blue: #4a9ad8;
    --wordmark: #2f6fb8;
  }
  * { margin: 0; padding: 0; box-sizing: border-box; }
  html, body {
    width: 900px;
    height: 1200px;
    overflow: hidden;
  }
  body {
    background: var(--stage);
    position: relative;
    font-family: "Lato", sans-serif;
  }
  .card {
    position: absolute;
    left: 85px;
    width: 733px;
    height: 428px;
    border-radius: 22px;
    overflow: hidden;
    background: var(--card);
  }
  .card-front {
    top: 138px;
    background: var(--sky);
  }
  .card-back { top: 634px; }

  .cloud-shape {
    position: absolute;
    inset: 0;
    width: 733px;
    height: 428px;
  }

  .front-wordmark {
    position: absolute;
    left: 80px;
    top: 256px;
    font-family: "Lato", sans-serif;
    font-weight: 700;
    font-size: 39px;
    letter-spacing: -0.5px;
    color: var(--wordmark);
  }

  .divider {
    position: absolute;
    left: 365px;
    top: 162px;
    width: 2px;
    height: 148px;
    background: var(--rule-grey);
  }

  .contact {
    position: absolute;
    left: 393px;
    top: 156px;
    color: var(--text-grey);
  }
  .person-name {
    font-family: "Raleway", sans-serif;
    font-weight: 700;
    font-size: 21px;
    color: var(--brand-blue);
    letter-spacing: 0.3px;
    line-height: 28px;
  }
  .person-role {
    font-family: "Raleway", sans-serif;
    font-weight: 700;
    font-size: 15px;
    color: var(--brand-green);
    letter-spacing: 0.4px;
    line-height: 20px;
  }
  .company-number {
    font-size: 16px;
    margin-top: 8px;
    line-height: 22px;
  }
  .contact-line {
    display: flex;
    align-items: center;
    font-size: 16px;
    line-height: 22px;
    margin-top: 6px;
  }
  .contact-line + .contact-line { margin-top: 2px; }
  .contact-icon {
    width: 15px;
    height: 15px;
    margin-right: 11px;
    flex: none;
  }
  .postal {
    font-size: 16px;
    line-height: 22px;
    margin-top: 6px;
  }

  .back-lockup {
    position: absolute;
    left: 170px;
    top: 180px;
    display: flex;
    align-items: center;
  }
  .back-mark {
    width: 34px;
    height: 34px;
    background: var(--icon-blue);
    margin-right: 20px;
    flex: none;
  }
  .back-wordmark {
    font-family: "Lato", sans-serif;
    font-weight: 700;
    font-size: 48px;
    letter-spacing: -0.5px;
    color: var(--wordmark);
    line-height: 52px;
  }
  .tagline {
    position: absolute;
    left: 291px;
    top: 240px;
    font-size: 13px;
    color: var(--text-grey);
    letter-spacing: 0.2px;
  }
</style>
</head>
<body>

<section class="card card-front">
  <svg class="cloud-shape" viewBox="0 0 733 428" aria-hidden="true">
    <defs>
      <linearGradient id="cloudFill" x1="0" y1="0" x2="0" y2="1">
        <stop offset="0.7" stop-color="#ffffff"/>
        <stop offset="1" stop-color="#eeeeee"/>
      </linearGradient>
    </defs>
    <path fill="url(#cloudFill)"
      d="M0 268
         C 15 250, 35 238, 57 233
         A 100 100 0 0 1 230 122
         A 214 214 0 0 1 642 192
         C 685 196, 715 220, 733 250
         L 733 428 L 0 428 Z"/>
  </svg>

  <div class="front-wordmark">TALBrookWare</div>

  <div class="divider"></div>

  <div class="contact">
    <div class="person-name">EWAN PARDOE</div>
    <div class="person-role">MANAGING DIRECTOR</div>
    <div class="company-number">A.C.N. 47 218 390 516</div>
    <div class="contact-line">
      <svg class="contact-icon" viewBox="0 0 15 15" aria-hidden="true">
        <rect width="15" height="15" rx="2" fill="var(--icon-blue)"/>
        <rect x="4.5" y="2.5" width="6" height="10" rx="1" fill="none" stroke="#fff" stroke-width="1.2"/>
        <circle cx="7.5" cy="10.5" r="0.8" fill="#fff"/>
      </svg>
      <span>0400-382-957</span>
    </div>
    <div class="contact-line">
      <svg class="contact-icon" viewBox="0 0 15 15" aria-hidden="true">
        <rect width="15" height="15" rx="2" fill="var(--icon-blue)"/>
        <rect x="3" y="4.5" width="9" height="6" fill="none" stroke="#fff" stroke-width="1.1"/>
        <path d="M3 4.5 L7.5 8 L12 4.5" fill="none" stroke="#fff" stroke-width="1.1"/>
      </svg>
      <span>Dermot@Talbrookware.example.com.au</span>
    </div>
    <div class="postal">PO Box 827, Harlowe Point 4291</div>
  </div>
</section>

<section class="card card-back">
  <div class="back-lockup">
    <div class="back-mark"></div>
    <div class="back-wordmark">TALBrookWare</div>
  </div>
  <div class="tagline">Lifted past the horizon</div>
</section>

</body>
</html>
```